依頼詳細
PCとスマホデザインの両方納品をいただきますが、
まずはデザインイメージが確認しやすいPCページのみの提案をお願いします。
スマホページは当選者に納品時にお願いしたいと思います。
スマホサイズについて、表示は横幅375pxで作成し、
デザインデータは2倍の横幅750pxのカンバスサイズで作成してください。
(Retinaディスプレイに対応するため)
レスポンシブウェブデザインを意識したデザインでお願いします。

■サイトマップ
添付の画面遷移図をご確認ください。

■参考サイト
https://www.kurumi-p.co.jp/
https://www.m-sorano.co.jp/
https://www.fujino-printing.co.jp/

■内容について
印刷会社のサイトリニューアルになります。
既存サイト
https://www.hinata-printing.co.jp/

■素材写真
画像データについては、フリー素材から流用して
イメージ画像に当て込んでください。
足りない場合は、一旦他のサイトの写真をサンプルとして
入れてください。(サンプルなどの表記をお願いします)
また、購入が必要な写真などを利用した場合、
価格とサイト名を教えてください。

また、Pixmora Stockで定期契約をしていますので、
Pixmora Stockの画像は使用できます。
デザイン時はカンプ画像をお入れいただきますようお願いします。

※採用サイト寄りのサイトにしたいので、使用する画像は
なるべく人物が入っているものを使用してください。

■ワイヤーフレーム
https://mock.plavetta.jp/view/51830427-216b-4c73-9a05-87162534907e-4182/?fullscreen
コンテンツの構成としてワイヤーフレームを作成しましたが
必ずしもワイヤーフレームの通りではなくて大丈夫です。
TOPページに配置するコンテンツを見ていただき、デザインは
デザイナーの皆様におまかせしたいと思います。

----------------------------------------------------------------------------
【制作物に対するお願い】

■フォントについて
・無料で使えるフォントで作成をお願いします。
・OSに紐づくフォントの使用は控えていただければと思います (ヒラギノなど)

ページ数
1ページ
希望イメージ
シンプル 複雑
単色 カラフル
暗い 明るい
日常 高級
遊び心 厳粛
未来的 伝統的
女性的 男性的
希望する色
青系、既存サイトに載っているロゴのイメージでお願いします。
納品ファイル
• 高解像度JPG (.jpg)
• イラストレーター形式 (.ai)
• フォトショップ形式 (.psd)
補足説明
上記のいずれか1つ(アウトラインありとなしの2つ)と高解像度JPGを納品お願いします。
adobe XDでの納品も可能です。

```html
<!DOCTYPE html>
<html lang="ja">
<head>
<meta charset="utf-8">
<title>ヒナタ印刷 | HINATA PRINTING</title>
<link href="https://fonts.googleapis.com/css2?family=Noto+Sans+JP:wght@400;500;700;900&display=swap" rel="stylesheet">
<style>
:root{
  --blue:#19a3e0;
  --yellow:#ffe600;
  --pink:#e6007e;
  --ink:#1a1a1a;
  --muted:#555;
  --dark:#1c1c1c;
  --paper:#ffffff;
  --line:#e2e2e2;
  --card-bg:#e6e6e6;
}
*{margin:0;padding:0;box-sizing:border-box}
html,body{width:1200px;height:3972px;overflow:hidden}
body{font-family:"Noto Sans JP",sans-serif;color:var(--ink);background:var(--paper);position:relative}

/* header */
.site-header{position:absolute;top:0;left:0;width:1200px;height:80px;z-index:5}
.brand{position:absolute;left:36px;top:18px;display:flex;align-items:center;gap:10px}
.brand-mark{width:30px;height:30px;background:var(--blue)}
.brand-name{font-size:24px;font-weight:900;color:var(--ink);line-height:1}
.brand-sub{font-size:9px;letter-spacing:.2em;color:var(--muted);margin-top:3px}
.global-nav{position:absolute;left:470px;top:0;height:80px;display:flex;align-items:center;gap:58px;font-size:14px;font-weight:500}
.nav-contact{position:absolute;right:0;top:0;width:180px;height:80px;background:var(--pink);color:#fff;font-size:14px;font-weight:700;display:flex;align-items:center;justify-content:center}

/* hero */
.hero-photo{position:absolute;top:0;left:0;width:1200px;height:760px;
  background:
    radial-gradient(ellipse 420px 260px at 78% 62%, rgba(250,250,248,.95), rgba(250,250,248,0) 70%),
    radial-gradient(ellipse 360px 300px at 28% 30%, rgba(58,62,70,.85), rgba(58,62,70,0) 70%),
    radial-gradient(ellipse 260px 160px at 46% 52%, rgba(214,178,150,.7), rgba(214,178,150,0) 70%),
    linear-gradient(135deg,#e4e4e2 0%,#b9babd 45%,#6c6f75 100%)}
.intro-box{position:absolute;left:120px;top:680px;width:970px;height:280px;background:#fff;display:flex;padding:50px 40px 0 40px}
.intro-title{width:380px;font-size:30px;font-weight:900;line-height:1.75;padding-top:56px}
.intro-text{flex:1;font-size:12.5px;line-height:2.1;color:var(--ink)}

/* service */
.service{position:absolute;top:1200px;left:0;width:1200px;height:370px;background:var(--blue);color:#fff}
.service h2{position:absolute;left:40px;top:70px;font-size:44px;font-weight:900}
.service p{position:absolute;left:40px;top:150px;width:570px;font-size:13px;line-height:1.9}
.btn-yellow{display:inline-flex;align-items:center;justify-content:center;background:var(--yellow);color:var(--ink);font-size:15px;font-weight:700}
.service .btn-yellow{position:absolute;left:40px;top:270px;width:170px;height:56px}
.service-photo{position:absolute;left:680px;top:88px;width:410px;height:200px;
  background:
    radial-gradient(ellipse 160px 90px at 58% 70%, rgba(232,90,120,.55), rgba(232,90,120,0) 70%),
    radial-gradient(ellipse 140px 90px at 78% 60%, rgba(250,190,60,.65), rgba(250,190,60,0) 70%),
    radial-gradient(ellipse 140px 80px at 40% 80%, rgba(70,160,220,.45), rgba(70,160,220,0) 70%),
    linear-gradient(160deg,#f6f6f4 0%,#dcd7d0 55%,#b9b2aa 100%)}

/* works */
.section-title{position:absolute;font-size:44px;font-weight:900;color:var(--ink)}
.works-more{position:absolute;left:950px;top:1806px;width:210px;height:56px}
.work-card{position:absolute;top:1930px;width:340px}
.work-img{height:320px;background:var(--card-bg);display:flex;justify-content:center;align-items:center}
.work-cover{width:230px;height:290px}
.work-card h3{font-size:13px;font-weight:700;margin-top:18px}
.work-card p{font-size:11px;color:var(--muted);margin-top:4px}

/* banners */
.banner{position:absolute;top:2520px;width:600px;height:280px;display:flex;align-items:flex-end;padding:0 0 44px 70px}
.banner span{font-size:52px;font-weight:900;color:var(--ink)}
.banner-company{left:0;background:
    radial-gradient(ellipse 200px 120px at 30% 40%, rgba(120,124,130,.55), rgba(120,124,130,0) 70%),
    linear-gradient(180deg,#f0f0f0 0%,#c9cbce 60%,#9da0a5 100%)}
.banner-upload{left:600px;background:
    radial-gradient(ellipse 220px 110px at 70% 30%, rgba(90,96,104,.45), rgba(90,96,104,0) 70%),
    linear-gradient(180deg,#f2f2f2 0%,#d6d7d9 60%,#b7b9bc 100%)}

/* news */
.sub-more{position:absolute;font-size:10px;color:var(--muted)}
.news-list{position:absolute;left:400px;top:2950px;width:760px;list-style:none}
.news-list li{display:flex;align-items:center;height:66px;border-bottom:1px solid var(--line)}
.news-date{width:140px;height:28px;background:var(--yellow);font-size:12px;font-weight:700;display:flex;align-items:center;justify-content:center;margin-right:34px}
.news-title{font-size:13px}

/* blog */
.blog-card{position:absolute;top:3330px;width:210px}
.blog-img{height:170px}
.blog-card time{display:block;font-size:10px;color:var(--muted);margin-top:12px}
.blog-card h3{font-size:13px;font-weight:700;margin-top:4px}
.blog-card p{font-size:10px;line-height:1.7;color:var(--muted);margin-top:6px}

/* footer */
.site-footer{position:absolute;top:3740px;left:0;width:1200px;height:232px;background:var(--dark);color:#fff}
.site-footer .brand{left:40px;top:46px}
.site-footer .brand-name{color:#fff}
.site-footer .brand-sub{color:#bbb}
.footer-info{position:absolute;left:330px;top:54px;font-size:12px;line-height:2}
.footer-links{position:absolute;left:330px;top:96px;display:flex;gap:22px;font-size:11px;color:#ccc}
.copyright{position:absolute;left:0;bottom:18px;width:1200px;text-align:center;font-size:10px;color:#aaa;border-top:1px solid #333;padding-top:16px}
</style>
</head>
<body>

<header class="site-header">
  <div class="brand">
    <div class="brand-mark"></div>
    <div>
      <div class="brand-name">ヒナタ印刷</div>
      <div class="brand-sub">HINATA PRINTING</div>
    </div>
  </div>
  <nav class="global-nav">
    <span>業務案内</span><span>入稿について</span><span>事例紹介</span><span>会社概要</span>
  </nav>
  <div class="nav-contact">お問い合わせ</div>
</header>

<div class="hero-photo" role="img" aria-label="印刷機から刷り上がった紙の束を両手で取り出す作業員の写真"></div>

<section class="intro-box">
  <h1 class="intro-title">ヒナタ印刷は<br>お客様と共に考えます。</h1>
  <p class="intro-text">新潟市の港町で創業して以来、チラシやパンフレット、ポスター、各種冊子など、地域の皆さまの「伝えたい」を形にしてまいりました。企画から印刷、加工、発送まで一貫して対応し、小ロットから大量印刷まで柔軟にお応えしています。印刷物はお客様の想いを届ける大切な道具です。だからこそ私たちは、ご要望を丁寧にうかがい、最適な紙や仕上がりをご提案することを大切にしています。これからも確かな技術と誠実なものづくりで、お客様と共に考え、歩み続ける会社でありたいと考えています。</p>
</section>

<section class="service">
  <h2>業務案内</h2>
  <p>ヒナタ印刷では、お客様の企画に合ったデザインから印刷、加工、発送までをまとめてお手伝いいたします。必要な部数や納期に合わせて最適な方法をご提案します。</p>
  <a class="btn-yellow">詳しく見る</a>
  <div class="service-photo" role="img" aria-label="色見本帳を広げてスタッフが打ち合わせをする手元の写真"></div>
</section>

<h2 class="section-title" style="left:40px;top:1796px">事例紹介</h2>
<a class="btn-yellow works-more">一覧を見る</a>

<article class="work-card" style="left:40px">
  <div class="work-img"><div class="work-cover" role="img" aria-label="赤い表紙に女性モデルが載るファッション雑誌の制作事例" style="background:radial-gradient(ellipse 90px 130px at 55% 62%,rgba(40,30,30,.55),rgba(40,30,30,0) 70%),linear-gradient(180deg,#e12a33,#8a1a22)"></div></div>
  <h3>ここに案件名が入ります</h3><p>ここにクライアント名が入ります</p>
</article>
<article class="work-card" style="left:430px">
  <div class="work-img"><div class="work-cover" role="img" aria-label="黄色い表紙に女性モデルが載るファッション雑誌の制作事例" style="background:radial-gradient(ellipse 80px 130px at 50% 60%,rgba(60,40,30,.45),rgba(60,40,30,0) 70%),linear-gradient(180deg,#f6cf2a,#c9962a)"></div></div>
  <h3>ここに案件名が入ります</h3><p>ここにクライアント名が入ります</p>
</article>
<article class="work-card" style="left:820px">
  <div class="work-img"><div class="work-cover" role="img" aria-label="白い表紙に女性モデルが載るファッション雑誌の制作事例" style="background:radial-gradient(ellipse 80px 130px at 55% 62%,rgba(50,50,56,.45),rgba(50,50,56,0) 70%),linear-gradient(180deg,#f7f7f7,#c9c9cc)"></div></div>
  <h3>ここに案件名が入ります</h3><p>ここにクライアント名が入ります</p>
</article>

<a class="banner banner-company" role="img" aria-label="社屋の外観写真"><span>会社概要</span></a>
<a class="banner banner-upload" role="img" aria-label="パソコンでデータを入稿するスタッフの作業風景の写真"><span>入稿について</span></a>

<h2 class="section-title" style="left:40px;top:2930px">新着情報</h2>
<span class="sub-more" style="left:42px;top:3006px">一覧を見る —</span>
<ul class="news-list">
  <li><span class="news-date">2022.10.28</span><span class="news-title">ホームページをリニューアルしました。</span></li>
  <li><span class="news-date">2022.9.17</span><span class="news-title">業務案内にデザイン制作を追加しました。</span></li>
  <li><span class="news-date">2022.8.1</span><span class="news-title">夏季休業のお知らせ</span></li>
</ul>

<h2 class="section-title" style="left:40px;top:3336px">ブログ</h2>
<span class="sub-more" style="left:42px;top:3412px">一覧を見る —</span>

<article class="blog-card" style="left:370px">
  <div class="blog-img" role="img" aria-label="会議室で社員が発表する全員会議の写真" style="background:radial-gradient(ellipse 70px 60px at 45% 55%,rgba(60,56,50,.5),rgba(60,56,50,0) 70%),linear-gradient(135deg,#d3cec4,#7d766c)"></div>
  <time>2022年10月20日</time><h3>全員会議を開催！</h3>
  <p>今期の目標を全員で共有しました。部署の垣根を越えた意見交換ができました。</p>
</article>
<article class="blog-card" style="left:630px">
  <div class="blog-img" role="img" aria-label="大勢の社員が参加する決算報告会の会場の写真" style="background:radial-gradient(ellipse 110px 50px at 50% 75%,rgba(70,66,62,.45),rgba(70,66,62,0) 70%),linear-gradient(135deg,#dedbd5,#8d8a86)"></div>
  <time>2022年9月28日</time><h3>決算報告会開催！</h3>
  <p>一年の歩みを振り返り、次の一年に向けた取り組みを確認しました。</p>
</article>
<article class="blog-card" style="left:890px">
  <div class="blog-img" role="img" aria-label="新しく導入した印刷機の写真" style="background:radial-gradient(ellipse 80px 50px at 50% 45%,rgba(255,255,255,.8),rgba(255,255,255,0) 70%),linear-gradient(135deg,#eeeeee,#b4b6b9)"></div>
  <time>2022年9月2日</time><h3>新たな機械が入りました</h3>
  <p>最新の印刷機を導入し、より鮮やかで早い仕上がりが可能になりました。</p>
</article>

<footer class="site-footer">
  <div class="brand">
    <div class="brand-mark"></div>
    <div>
      <div class="brand-name">ヒナタ印刷</div>
      <div class="brand-sub">HINATA PRINTING</div>
    </div>
  </div>
  <p class="footer-info">〒950-0000 新潟県みどり市港町1-2-3　株式会社ヒナタ印刷　TEL：0250-00-1234　FAX：0250-00-1235</p>
  <div class="footer-links"><span>お問い合わせ</span><span>プライバシーポリシー</span><span>採用情報</span><span>サイトマップ</span></div>
  <p class="copyright">Copyright © 株式会社 ヒナタ印刷</p>
</footer>

</body>
</html>
```